Wrenfield food and drinks menu

Tamarind on Vellory is a vegan restaurant in NYC. It's food menu is given to guests on a casual clipboard, on regular sized 8.5 x 11 sheets of paper.

The assignment is to create a drinks menu to make the cocktail, wine and beer offerings more prominent. The drinks menu should be half the size of the regular menu so it sits smaller on top of the 8.5 x 11 sheet of paper. Other requirements:

-Please refer to the website design for inspiration and style guide
wrenfieldeats.com
-brand assets, the logo for Tamarind on Vellory and color treatments are here
https://www.filecrate.example/sh/8kqpwz2lmtdfa/QXvbnPzr4T
- if there is too much copy the drinks menu can be laid out on a 8.5 x 11 sheet of paper that opens like a book horizontally, with a front cover, then the inside left and right panels and back panel can have text.

The drinks menu should be organized by:

Organic Cocktails
Wines by the glass (white, red, rose)
Sparkling
Beer
Non alcoholic

List of drinks are enclosed

Industry/Entity Type

Restaurant

Requirements
Must have
• Tamarind on Vellory logo, and all the drink items listed in the attached menu.
Use fonts that are in the brand asset dropbox.
Should not have
• Lots of color. This will most likely not be printed in color.

```html
<!DOCTYPE html>
<html lang="en">
<head>
<meta charset="utf-8">
<title>Wrenfield food and drinks menu</title>
<link rel="stylesheet" href="https://fonts.googleapis.com/css2?family=Open+Sans:ital,wght@0,400;0,600;1,400&family=Cinzel:wght@400&display=swap">
<style>
  :root {
    --canvas: #ffffff;
    --frame: #d9d9d9;
    --cover-green: #4a6352;
    --paper: #f3efe8;
    --ink: #555a55;
    --label: #4d6355;
    --citron: #cbc21a;
    --leaf: #8dc43f;
    --forest: #3f5a48;
    --logo-white: #f4f4ef;
  }
  * { margin: 0; padding: 0; box-sizing: border-box; }
  html, body { width: 1200px; height: 423px; overflow: hidden; background: var(--canvas); }
  .board {
    position: relative; width: 1200px; height: 423px;
    border: 1px solid var(--frame);
    font-family: "Open Sans", Arial, sans-serif; color: var(--ink);
  }
  .section-label {
    position: absolute; font-size: 13px; color: var(--label);
    transform: translateX(-50%); white-space: nowrap;
  }
  .section-label--covers { left: 302px; top: 26px; }
  .section-label--menus { left: 931px; top: 31px; }

  .panel { position: absolute; top: 63px; width: 242px; height: 314px; }
  .cover { background: var(--cover-green); }
  .cover--front { left: 51px; }
  .cover--back { left: 319px; }
  .cover__name {
    position: absolute; top: 138px; left: 0; width: 100%; text-align: center;
    font-family: "Cinzel", Georgia, serif; font-size: 15px; letter-spacing: 1px;
    color: var(--logo-white);
  }

  .page { background: var(--paper); overflow: hidden; }
  .page--food { left: 645px; }
  .page--drinks { left: 915px; }
  .page__rule { position: absolute; left: 0; top: 24px; width: 100%; height: 2px; background: var(--citron); }
  .page__band { position: absolute; left: 0; bottom: 0; width: 100%; height: 7px; background: var(--leaf); }
  .page__brand {
    position: absolute; left: 9px; top: 12px;
    font-family: "Cinzel", Georgia, serif; font-size: 8px; color: var(--forest); letter-spacing: .5px;
  }

  .line {
    position: absolute; left: 14px; right: 14px; text-align: center;
    font-size: 5.2px; line-height: 7px;
  }
  .heading { font-size: 6.8px; font-weight: 600; }
  .thanks { font-size: 8px; font-style: italic; }

  .swatch { position: absolute; top: 148px; width: 13px; height: 13px; border-radius: 50%; }
  .swatch--citron { left: 85px; background: var(--citron); }
  .swatch--leaf { left: 115px; background: var(--leaf); }
  .swatch--forest { left: 145px; background: var(--forest); }
</style>
</head>
<body>
<main class="board">
  <p class="section-label section-label--covers">Cover and back cover</p>
  <p class="section-label section-label--menus">food menu and drink menu</p>

  <section class="panel cover cover--front" aria-label="Front cover">
    <p class="cover__name">Tamarind on Vellory</p>
  </section>
  <section class="panel cover cover--back" aria-label="Back cover"></section>

  <section class="panel page page--food" aria-label="Food menu">
    <p class="page__brand">Tamarind on Vellory</p>
    <div class="page__rule"></div>
    <p class="line heading" style="top:42px">Large plates</p>
    <p class="line" style="top:63px">sliders ~ seitan /mushroom patty, poblano 1000 island,fried onion, lettuce,<br>tomato, pickle, served with your choice of field greens or french fries ~ 14 (nf)</p>
    <p class="line" style="top:82px">pasta ~ elbow macaroni, artichoke hearts, english peas, truffled cashew cream,<br>mint pesto ~ 16</p>
    <p class="line" style="top:101px">pizza ~ plum tomato ragout, cashew ricotta, mozzarella, smoked fennel, pesto,<br>arugula ~ 14</p>
    <p class="line" style="top:120px">tagine ~ orange scented millet, chickpeas, dried apricots, oil-cured olives,<br>moroccan spiced tomato broth ~ 17 (gf, nf, sf)</p>
    <p class="line" style="top:139px">piccata ~ pan-seared seitan cutlets, lemon/white wine butter, fried capers ~ 19</p>
    <p class="line" style="top:152px">marsala ~ pan seared seitan cutlets, spicy marsala pan sauce,<br>fingerling au ratin potatoes, sautéed kale ~ 19</p>
    <p class="line heading" style="top:186px">sweets</p>
    <p class="line" style="top:214px">chocolate truffles "of the moment" ~ 10</p>
    <p class="line" style="top:228px">strawberry short cake, fresh crème and strawberries, vanilla ice cream ~ 10 (nf)</p>
    <p class="line" style="top:240px">peach and strawberry crumble, vanilla ice cream ~ 9 (nf)</p>
    <p class="line" style="top:252px">new york cheesecake, peach reduction, chocolate chips ~ 11 (nf)</p>
    <p class="line" style="top:264px">blueberry bread pudding, vanilla glaze, fresh blueberries ~ 9 (nf)</p>
    <div class="page__band"></div>
  </section>

  <section class="panel page page--drinks" aria-label="Drink menu">
    <div class="page__rule"></div>
    <p class="line heading" style="top:42px">Drinks</p>
    <p class="line" style="top:59px">Organic Cocktails</p>
    <p class="line" style="top:70px">Wines by the glass (white, red, rose)</p>
    <p class="line" style="top:81px">Sparkling</p>
    <p class="line" style="top:92px">Beer</p>
    <p class="line" style="top:103px">Non alcoholic</p>
    <p class="line" style="top:122px">executive chef : Daniel Morrow</p>
    <span class="swatch swatch--citron"></span>
    <span class="swatch swatch--leaf"></span>
    <span class="swatch swatch--forest"></span>
    <p class="line" style="top:180px">gf = gluten free, nf = nut free, sf = soy free</p>
    <p class="line" style="top:202px">a 20% gratuity is applied to parties of five or more</p>
    <p class="line" style="top:219px">all of our offerings are completely free of any animal products<br>and ar organic and/or local as possible</p>
    <p class="line thanks" style="top:262px">thanks for dining with us!</p>
    <div class="page__band"></div>
  </section>
</main>
</body>
</html>
```